Magazine advertisement

I need a company advertisement for magazine prints. I need to be able to scale it to different sizes if need be. I need it to showcase our brand, VornaDrive have our phone number 582.463.9047 our contact email address sales@vornadrive.net and web address www.vornadrive.net

Target Market(s)

automotive / tractor pulling

Industry/Entity Type

automotive / racing

Colors
EB3D1F
EC4F4E
F09395
F8D3D4
FCEDEE

Requirements
Must have
• our logo, our color scheme (pantone red 1795, white, black, silver

```html
<!DOCTYPE html>
<html lang="en">
<head>
<meta charset="UTF-8">
<title>VornaDrive Magazine Advertisement</title>
<link href="https://fonts.googleapis.com/css2?family=Black+Ops+One&family=Poppins:wght@400;600;700&display=swap" rel="stylesheet">
<style>
  :root {
    --red: #EB3D1F;
    --red-soft: #EC4F4E;
    --red-deep: #b3121c;
    --red-dark: #5a0a0f;
    --pink: #F09395;
    --blush: #F8D3D4;
    --white: #ffffff;
    --black: #0b0b0c;
    --silver: #d4d4d7;
    --grey: #6e6e72;
    --stage: #e4e4e6;
  }
  * { box-sizing: border-box; margin: 0; padding: 0; }
  html, body {
    width: 1200px; height: 495px; overflow: hidden;
    background: var(--stage);
  }
  .ad {
    position: absolute; left: 422px; top: 17px;
    width: 356px; height: 460px;
    background: var(--black);
    overflow: hidden;
    font-family: "Poppins", sans-serif;
    color: var(--white);
  }
  .ad-backdrop { position: absolute; inset: 0; }
  .brand {
    position: absolute; top: 52px; left: 0; right: 0;
    display: flex; justify-content: center; align-items: center; gap: 7px;
  }
  .brand-mark { width: 11px; height: 11px; background: var(--red); }
  .brand-name {
    font-weight: 600; font-size: 22px; letter-spacing: 3px; color: var(--white);
  }
  .headline-band {
    position: absolute; top: 90px; left: 0; width: 356px; height: 45px;
    background: linear-gradient(90deg, var(--red-deep) 0%, var(--red) 45%, var(--red-soft) 70%, var(--red-dark) 100%);
  }
  .headline {
    position: absolute; top: 94px; left: 0; right: 0; text-align: center;
    font-family: "Black Ops One", sans-serif; font-weight: 400; font-size: 19px;
    line-height: 19px; letter-spacing: 0.6px; color: var(--white);
  }
  .tagline-band {
    position: absolute; top: 141px; left: 0; width: 356px; height: 29px;
    background: linear-gradient(90deg, rgba(110,110,114,0) 0%, rgba(110,110,114,0.55) 40%, rgba(150,150,154,0.8) 100%);
  }
  .tagline {
    position: absolute; top: 145px; left: 0; right: 0; text-align: center;
    font-weight: 600; font-size: 8px; line-height: 10px;
  }
  .product-photo {
    position: absolute; left: 28px; top: 180px; width: 300px; height: 252px;
    background: linear-gradient(180deg, #e2e2e4 0%, #a7a7ac 38%, #c4161f 62%, #7a0d14 84%, #2a2a2c 100%);
    clip-path: polygon(24% 0, 76% 0, 76% 48%, 100% 60%, 100% 100%, 0 100%, 0 60%, 24% 48%);
  }
  .feature {
    position: absolute; top: 200px; white-space: nowrap;
  }
  .feature-left { left: 15px; text-align: left; }
  .feature-right { right: 15px; text-align: right; }
  .feature-title { font-weight: 700; font-size: 8px; line-height: 10px; margin-bottom: 2px; }
  .feature-body { font-size: 6.2px; line-height: 7.6px; }
  .contact-bar {
    position: absolute; top: 440px; left: 0; width: 356px; height: 13px;
    background: linear-gradient(90deg, var(--grey) 0%, #1b1b1d 12%, #1b1b1d 88%, var(--grey) 100%);
    display: flex; justify-content: center; align-items: center; gap: 14px;
  }
  .contact-item { display: flex; align-items: center; gap: 4px; font-size: 7px; font-weight: 600; }
  .contact-phone { font-size: 9.5px; }
  .contact-icon { width: 7px; height: 7px; }
</style>
</head>
<body>
  <main class="ad">
    <svg class="ad-backdrop" viewBox="0 0 356 460" aria-hidden="true">
      <defs>
        <linearGradient id="streak" x1="0" y1="0" x2="1" y2="1">
          <stop offset="0" stop-color="#EB3D1F" stop-opacity="0.9"/>
          <stop offset="1" stop-color="#5a0a0f" stop-opacity="0"/>
        </linearGradient>
        <linearGradient id="panel-left" x1="0" y1="0" x2="1" y2="0">
          <stop offset="0" stop-color="#c4161f"/>
          <stop offset="0.7" stop-color="#c4161f" stop-opacity="0.85"/>
          <stop offset="1" stop-color="#c4161f" stop-opacity="0"/>
        </linearGradient>
        <linearGradient id="panel-right" x1="1" y1="0" x2="0" y2="0">
          <stop offset="0" stop-color="#c4161f"/>
          <stop offset="0.7" stop-color="#c4161f" stop-opacity="0.85"/>
          <stop offset="1" stop-color="#c4161f" stop-opacity="0"/>
        </linearGradient>
        <linearGradient id="silver" x1="0" y1="0" x2="1" y2="1">
          <stop offset="0" stop-color="#f2f2f3"/>
          <stop offset="1" stop-color="#8d8d92"/>
        </linearGradient>
      </defs>
      <rect width="356" height="460" fill="#0b0b0c"/>
      <polygon points="190,0 356,0 356,70 300,0" fill="url(#streak)"/>
      <polygon points="240,0 275,0 356,60 356,85" fill="url(#streak)" opacity="0.7"/>
      <polygon points="0,0 60,0 0,40" fill="#7a0d14" opacity="0.7"/>
      <polygon points="0,170 140,170 0,230" fill="url(#streak)" opacity="0.6"/>
      <polygon points="250,170 356,170 356,215" fill="url(#streak)" opacity="0.5"/>
      <rect x="0" y="192" width="120" height="104" fill="url(#panel-left)"/>
      <rect x="236" y="192" width="120" height="104" fill="url(#panel-right)"/>
      <polygon points="0,405 130,352 0,430" fill="url(#silver)" opacity="0.8"/>
      <polygon points="0,430 160,360 0,440" fill="#ffffff"/>
      <polygon points="356,372 356,425 245,342" fill="url(#silver)" opacity="0.85"/>
    </svg>

    <div class="product-photo" role="img" aria-label="Photo of a polished silver turbocharger above a red pulling tractor in motion"></div>

    <div class="brand">
      <span class="brand-mark"></span>
      <span class="brand-name">VORNADRIVE</span>
    </div>

    <div class="headline-band"></div>
    <h1 class="headline">MAXIMUM PERFORMANCE<br>ULTIMATE POWER</h1>

    <div class="tagline-band"></div>
    <p class="tagline">Specializing in high-performance turbochargers for automotive<br>racing and tractor pulling.</p>

    <section class="feature feature-left">
      <h2 class="feature-title">Built to Win</h2>
      <p class="feature-body">We'll help you perform<br>like a winner, from<br>truck and tractor<br>pulling to drag racing.<br>Our turbochargers are<br>equipped with the<br>capacity to power<br>everything from<br>high-end sports cars<br>to snowmobiles.</p>
    </section>

    <section class="feature feature-right">
      <h2 class="feature-title">One Fierce Turbine</h2>
      <p class="feature-body">Our hub-free<br>design maximizes<br>aerodynamics and has<br>been dyno-proven to<br>yield maximum<br>horsepower without<br>the need to increase<br>frame size.</p>
    </section>

    <footer class="contact-bar">
      <span class="contact-item contact-phone">
        <svg class="contact-icon" viewBox="0 0 10 10"><path d="M2 1 L4 1 L4.6 3.2 L3.4 4 Q4.4 6 6 6.6 L6.8 5.4 L9 6 L9 8 Q9 9 8 9 Q1 8.6 1 2 Q1 1 2 1 Z" fill="#EB3D1F"/></svg>
        582.463.9047
      </span>
      <span class="contact-item">
        <svg class="contact-icon" viewBox="0 0 10 10"><rect x="0.5" y="2" width="9" height="6" fill="#EB3D1F"/><path d="M0.5 2 L5 5.5 L9.5 2" stroke="#ffffff" stroke-width="0.8" fill="none"/></svg>
        sales@vornadrive.net
      </span>
      <span class="contact-item">
        <svg class="contact-icon" viewBox="0 0 10 10"><circle cx="5" cy="5" r="4.2" fill="none" stroke="#EB3D1F" stroke-width="1"/><ellipse cx="5" cy="5" rx="1.8" ry="4.2" fill="none" stroke="#EB3D1F" stroke-width="0.8"/><line x1="0.8" y1="5" x2="9.2" y2="5" stroke="#EB3D1F" stroke-width="0.8"/></svg>
        www.vornadrive.net
      </span>
    </footer>
  </main>
</body>
</html>
```